hair salon logo and Business Card Design

this logo needs to reflect a vibrant, trendy and fun business, targeting 20 to 50 year old ladies in a nice sunny part of Australia.Our aim is to make everyone feel in a fantastic mood when they walk out of the salon,and look equally glamorous.
I would like the logo to be simple yet using bold colors and font.
ideally the name mirra would be lowercase with a nice rounded shape and hair+beauty, with upper case and the letter i in an inverted position.

Industry/Entity Type

Hair

Contact Information for Business Card

mirra
hair | beauty.

Lia Forsett
stylist/owner
0419376052
58 Wexcombe St. Scarborough QLD. 4020

Requirements
Must have
• front all the business details
back lined for writing notes.
Nice to have
• use of bold stand out colors, simple shapes sense of movement, not stillness, modern, professional.

```html
<!DOCTYPE html>
<html lang="en">
<head>
<meta charset="utf-8">
<title>mirra hair | beauty – business card</title>
<link rel="stylesheet" href="https://fonts.googleapis.com/css2?family=Barlow:wght@300;400;600;700&display=swap">
<style>
  :root {
    --cream: #fcf6ef;
    --teal: #009fb2;
    --brown: #5a2b0a;
    --grey: #8f959b;
    --peach: #fcc58f;
  }
  html, body {
    margin: 0;
    padding: 0;
    overflow: hidden;
    background: var(--cream);
  }
  .card {
    position: relative;
    width: 1200px;
    height: 740px;
    background: var(--cream);
    overflow: hidden;
    font-family: "Barlow", Arial, sans-serif;
  }
  .brand-artwork {
    position: absolute;
    left: 0;
    top: 50px;
    width: 440px;
    height: 505px;
  }
  .brand-name {
    position: absolute;
    left: 226px;
    top: 87px;
    margin: 0;
    font-size: 150px;
    line-height: 1;
    font-weight: 600;
    letter-spacing: -2px;
    color: var(--teal);
  }
  .brand-tagline {
    position: absolute;
    right: 92px;
    top: 167px;
    margin: 0;
    font-size: 54px;
    line-height: 1;
    font-weight: 300;
    letter-spacing: 0.2em;
    color: var(--brown);
    display: flex;
    align-items: center;
  }
  .brand-tagline .word:last-child {
    margin-right: -0.2em;
  }
  .brand-tagline .divider {
    display: inline-block;
    width: 4px;
    height: 46px;
    margin: 0 40px 0 28px;
    background: var(--teal);
  }
  .contact {
    position: absolute;
    right: 92px;
    margin: 0;
    line-height: 1;
    text-align: right;
    white-space: nowrap;
  }
  .contact-name {
    top: 301px;
    font-size: 54px;
    font-weight: 700;
    color: var(--brown);
    letter-spacing: -0.5px;
  }
  .contact-role {
    top: 357px;
    font-size: 42px;
    font-weight: 400;
    color: var(--grey);
  }
  .contact-role .dot {
    display: inline-block;
    width: 10px;
    height: 10px;
    margin: 0 14px 6px;
    background: var(--teal);
  }
  .contact-phone {
    top: 429px;
    font-size: 48px;
    font-weight: 700;
    color: var(--grey);
    letter-spacing: 0.5px;
  }
  .contact-address {
    font-size: 46px;
    font-weight: 300;
    color: var(--grey);
  }
  .address-street { top: 524px; }
  .address-suburb { top: 572px; }
  .footer-band {
    position: absolute;
    left: 0;
    bottom: 0;
    width: 1200px;
    height: 92px;
    background: var(--teal);
  }
</style>
</head>
<body>
  <div class="card">
    <svg class="brand-artwork" viewBox="0 0 440 505" role="img" aria-label="Brand artwork: flowing hair strands in brown and teal with scattered peach dots">
      <defs>
        <radialGradient id="artwork-glow" cx="0.45" cy="0.45" r="0.6">
          <stop offset="0" stop-color="#fcc58f" stop-opacity="0.75"/>
          <stop offset="0.6" stop-color="#9fd3d6" stop-opacity="0.35"/>
          <stop offset="1" stop-color="#fcf6ef" stop-opacity="0"/>
        </radialGradient>
      </defs>
      <rect width="440" height="505" fill="url(#artwork-glow)"/>
    </svg>

    <h1 class="brand-name">mirra</h1>
    <p class="brand-tagline"><span class="word">HAIR</span><span class="divider"></span><span class="word">BEAUTY</span></p>

    <p class="contact contact-name">Lia Forsett</p>
    <p class="contact contact-role">stylist<span class="dot"></span>owner</p>
    <p class="contact contact-phone">0419 376 052</p>
    <p class="contact contact-address address-street">58 Wexcombe Street</p>
    <p class="contact contact-address address-suburb">Tallowmere, QLD 4027</p>

    <div class="footer-band"></div>
  </div>
</body>
</html>
```